Venture Capital Investment Firm

We are looking to overhaul our existing website (substantially), with only using the same logos (which we can provide).
We are an investment firm that focuses on making loans to late stage technology companies. Our site should ultimately look like other venture capital firms, and look modern and fresh. We have an existing website www.brenvoltfund.com which this will be replacing, although we will be using a lot of the existing written content, and potentially the numbers of pages we will need, we are not wed to anything else. Please feel free to shoot any questions at any time and thank you in advance for your help!
Websites we like as examples:
https://www.tarnwickbay.com/
https://www.morrowlanefinance.com/
Target Market(s)
Potential investors who will invest in our firm, as well as potentially companies that are looking to borrow money from us.
Coding
Colors
Look and feel

```html
<!DOCTYPE html>
<html lang="en">
<head>
<meta charset="utf-8">
<title>News – Brenvolt Fund</title>
<link href="https://fonts.googleapis.com/css2?family=Nunito:wght@400;600;700;800&family=Arimo:wght@400;500&display=swap" rel="stylesheet">
<style>
:root{
  --navy:#07073f;
  --navy-deep:#05053a;
  --ink:#1d2b4f;
  --heading:#1f3a66;
  --muted:#777;
  --blue:#2f8fd3;
  --blue-light:#4aa8e3;
  --card-border:#d3e9f6;
  --white:#fff;
}
*{box-sizing:border-box;margin:0;padding:0}
html,body{width:1200px;height:2245px;overflow:hidden}
body{font-family:"Nunito",sans-serif;color:var(--ink);background:var(--white);position:relative}
a{color:inherit;text-decoration:none}

.site-header{position:absolute;top:0;left:0;width:1200px;height:151px}
.brand{position:absolute;left:80px;top:26px;display:flex;align-items:center;gap:12px}
.brand-dot{width:40px;height:40px;border-radius:50%;background:var(--navy)}
.brand-name{font-size:30px;font-weight:700;color:var(--navy);letter-spacing:.5px}
.contact-item{position:absolute;top:31px;display:flex;gap:14px;align-items:flex-start;font-size:14px;line-height:14px}
.contact-item svg{margin-top:6px}
.contact-item strong{display:block;font-weight:700;color:#111;font-size:13px}
.contact-item span{color:#555}
.contact-email{left:598px}
.contact-call{left:873px}
.main-nav{position:absolute;top:102px;left:80px;display:flex;font-family:"Arimo",sans-serif;font-size:11.5px;color:#111}
.main-nav a{padding:17px 18px 0;height:40px;border-top:2px solid transparent}
.main-nav a.active{border-top-color:var(--navy)}

.page-banner{position:absolute;top:151px;left:0;width:1200px;height:94px;background:linear-gradient(90deg,#2f6fb0,#3b8fd0 55%,#2c9de0);text-align:center;color:var(--white)}
.page-banner h1{font-size:38px;font-weight:800;margin-top:6px;line-height:48px}
.breadcrumb{font-size:13px;font-weight:600;letter-spacing:.5px;margin-top:12px;display:flex;justify-content:center;gap:12px}
.breadcrumb a{border-bottom:1px solid rgba(255,255,255,.6);padding-bottom:2px}

.news{position:absolute;top:245px;left:0;width:1200px;height:1476px}
.news-title{position:absolute;top:34px;width:100%;text-align:center;font-size:32px;font-weight:700;color:var(--heading)}
.news-grid{position:absolute;top:152px;left:80px;width:1040px;display:grid;grid-template-columns:repeat(3,327px);column-gap:29px;row-gap:30px;align-items:start}
.news-card{border:4px solid var(--card-border);background:var(--white)}
.news-media{position:relative;height:257px}
.news-media .photo{position:absolute;inset:0}
.photo-a{background:linear-gradient(135deg,#3a4a66,#c9d3d8 55%,#e9eef0)}
.photo-b{background:linear-gradient(135deg,#d7dee4,#a9bdd2 50%,#6e7f92)}
.photo-c{background:linear-gradient(135deg,#cfd6d9,#8b97a3 55%,#2a3346)}
.news-date{position:absolute;left:0;bottom:0;width:44px;height:92px;background:var(--navy);color:var(--white);text-align:center;padding-top:10px;font-size:12.5px;line-height:22px}
.news-date b{display:block;font-size:19px;font-weight:700;line-height:26px}
.news-body{padding:22px 22px 24px}
.news-body h2{font-size:19px;font-weight:400;line-height:28px;color:#111}
.news-body p{margin-top:14px;font-size:15px;line-height:27px;color:var(--muted)}
.read-more{display:inline-flex;align-items:center;gap:4px;margin-top:22px;height:35px;padding:0 12px;border-radius:18px;background:var(--navy);color:var(--white);font-size:15px}

.pagination{position:absolute;top:1405px;left:457px;display:flex;gap:4px}
.pagination a{width:37px;height:37px;border-radius:50%;border:1px solid var(--card-border);display:flex;align-items:center;justify-content:center;font-family:"Arimo",sans-serif;font-size:14px;color:#222}
.pagination a.current{background:var(--navy);border-color:var(--navy);color:var(--white)}

.cta-band{position:absolute;top:1721px;left:0;width:1200px;height:144px;background:linear-gradient(90deg,#2f74b8,#3a90d2 50%,#41a6e2)}
.cta-band h2{position:absolute;left:80px;top:50px;font-size:33px;font-weight:700;color:var(--white)}
.cta-button{position:absolute;left:882px;top:45px;width:238px;height:54px;border-radius:27px;background:var(--white);color:var(--heading);font-size:15px;display:flex;align-items:center;justify-content:center}

.site-footer{position:absolute;top:1865px;left:0;width:1200px;height:380px;background:var(--navy-deep);color:var(--white)}
.footer-col{position:absolute;top:30px}
.footer-col h3{font-size:19px;font-weight:700}
.col-reach{left:80px;width:320px}
.col-links{left:459px}
.col-connect{left:614px}
.col-subscribe{left:881px;width:239px}
.reach-list{list-style:none;margin-top:40px;font-size:13.5px;line-height:19px}
.reach-list li{display:flex;gap:20px;margin-bottom:22px}
.reach-list svg{flex:none;margin-top:2px}
.link-list{list-style:none;margin-top:44px;font-size:13.5px;line-height:23px}
.link-list li{display:flex;align-items:center;gap:6px}
.social{display:flex;gap:12px;margin-top:20px}
.social span{width:38px;height:38px;border-radius:50%;background:#16164f;display:flex;align-items:center;justify-content:center}
.social span i{width:10px;height:10px;border-radius:50%;background:var(--white)}
.subscribe-input{margin-top:46px;height:48px;background:#16164f;display:flex;align-items:center;justify-content:center;font-size:15px;color:#d8d8e6}
.subscribe-btn{margin-top:8px;height:48px;background:#7a7a7f;display:flex;align-items:center;justify-content:center;font-size:15px}
.copyright{position:absolute;top:319px;width:100%;text-align:center;font-size:13.5px;color:#d0d0dd}
</style>
</head>
<body>

<header class="site-header">
  <a class="brand" href="#"><span class="brand-dot"></span><span class="brand-name">BRENVOLT FUND</span></a>
  <div class="contact-item contact-email">
    <svg width="20" height="18" viewBox="0 0 20 18"><path d="M19 1 1 8l6 2 2 7 3-5 5 3z" fill="var(--navy)"/></svg>
    <div><strong>Email</strong><span>hello@brenvoltfund.com</span></div>
  </div>
  <div class="contact-item contact-call">
    <svg width="16" height="16" viewBox="0 0 16 16"><path d="M3 1h3l1.5 4-2 1.3a9 9 0 0 0 4.2 4.2L11 8.5l4 1.5v3a2 2 0 0 1-2 2A13 13 0 0 1 1 3a2 2 0 0 1 2-2z" fill="var(--navy)"/></svg>
    <div><strong>Call</strong><span>Call Us: + 1240 5581 37</span></div>
  </div>
  <nav class="main-nav">
    <a href="#">HOME</a><a href="#">STRATEGY</a><a href="#" class="active">ABOUT US</a><a href="#">TEAM</a><a href="#">NEWS</a><a href="#">CAREER</a><a href="#">CONTACT</a><a href="#">INVESTORS</a>
  </nav>
</header>

<section class="page-banner">
  <h1>News</h1>
  <div class="breadcrumb"><a href="#">HOME ›</a><a href="#">NEWS ›</a></div>
</section>

<main class="news">
  <h2 class="news-title">Latest News</h2>
  <div class="news-grid">
    <article class="news-card">
      <div class="news-media"><div class="photo photo-a" role="img" aria-label="Business meeting at a desk with laptop and documents"></div><div class="news-date"><b>30</b>April<br>2018</div></div>
      <div class="news-body"><h2>Brenvolt Fund completes structured debt investment in Fernbrook</h2><p>Far far away, behind the word mountains, far from the countries Vokalia and Consonantia, there live the blind texts.</p><a class="read-more" href="#">Read More →</a></div>
    </article>
    <article class="news-card">
      <div class="news-media"><div class="photo photo-b" role="img" aria-label="Team of colleagues reviewing a document together"></div><div class="news-date"><b>06</b>April<br>2016</div></div>
      <div class="news-body"><h2>Halvern Semiconductor acquired by Quillmark for $55,000,000</h2><p>Far far away, behind the word mountains, far from the countries Vokalia and Consonantia, there live the blind texts.</p><a class="read-more" href="#">Read More →</a></div>
    </article>
    <article class="news-card">
      <div class="news-media"><div class="photo photo-c" role="img" aria-label="Two businessmen in suits discussing at an office table"></div><div class="news-date"><b>19</b>OCT<br>2016</div></div>
      <div class="news-body"><h2>Brenvolt Fund completes $22,000,000 structured debt investment in Surveyline</h2><p>Far far away, behind the word mountains, far from the countries Vokalia and Consonantia, there live the blind texts.</p><a class="read-more" href="#">Read More →</a></div>
    </article>
    <article class="news-card">
      <div class="news-media"><div class="photo photo-a" role="img" aria-label="Business meeting at a desk with laptop and documents"></div><div class="news-date"><b>30</b>April<br>2018</div></div>
      <div class="news-body"><h2>Brenvolt Fund completes structured debt investment in Fernbrook</h2><p>Far far away, behind the word mountains, far from the countries Vokalia and Consonantia, there live the blind texts.</p><a class="read-more" href="#">Read More →</a></div>
    </article>
    <article class="news-card">
      <div class="news-media"><div class="photo photo-b" role="img" aria-label="Team of colleagues reviewing a document together"></div><div class="news-date"><b>06</b>April<br>2016</div></div>
      <div class="news-body"><h2>Halvern Semiconductor acquired by Quillmark for $55,000,000</h2><p>Far far away, behind the word mountains, far from the countries Vokalia and Consonantia, there live the blind texts.</p><a class="read-more" href="#">Read More →</a></div>
    </article>
    <article class="news-card">
      <div class="news-media"><div class="photo photo-c" role="img" aria-label="Two businessmen in suits discussing at an office table"></div><div class="news-date"><b>19</b>OCT<br>2016</div></div>
      <div class="news-body"><h2>Brenvolt Fund completes $22,000,000 structured debt investment in Surveyline</h2><p>Far far away, behind the word mountains, far from the countries Vokalia and Consonantia, there live the blind texts.</p><a class="read-more" href="#">Read More →</a></div>
    </article>
  </div>
  <nav class="pagination">
    <a href="#">&lt;</a><a href="#" class="current">1</a><a href="#">2</a><a href="#">3</a><a href="#">4</a><a href="#">5</a><a href="#">&gt;</a>
  </nav>
</main>

<section class="cta-band">
  <h2>You Always Get the Best Guidance</h2>
  <a class="cta-button" href="#">Connect Us</a>
</section>

<footer class="site-footer">
  <div class="footer-col col-reach">
    <h3>Reach Us</h3>
    <ul class="reach-list">
      <li><svg width="17" height="17" viewBox="0 0 12 16"><path d="M6 0a6 6 0 0 1 6 6c0 4-6 10-6 10S0 10 0 6a6 6 0 0 1 6-6zm0 3.5a2.5 2.5 0 1 0 0 5 2.5 2.5 0 0 0 0-5z" fill="#fff"/></svg><span>418 Alder Row, Palo Verde,<br>California, USA</span></li>
      <li><svg width="17" height="17" viewBox="0 0 16 16"><path d="M3 1h3l1.5 4-2 1.3a9 9 0 0 0 4.2 4.2L11 8.5l4 1.5v3a2 2 0 0 1-2 2A13 13 0 0 1 1 3a2 2 0 0 1 2-2z" fill="#fff"/></svg><span>+2 415 7720 318</span></li>
      <li style="margin-top:30px"><svg width="17" height="14" viewBox="0 0 17 14"><path d="M0 1h17v12H0zM0 1l8.5 6L17 1" fill="#fff" stroke="var(--navy-deep)" stroke-width="1.2"/></svg><span>info@brenvoltfund.com</span></li>
    </ul>
  </div>
  <div class="footer-col col-links">
    <h3>Links</h3>
    <ul class="link-list">
      <li>→ <a href="#">Home</a></li><li>→ <a href="#">About</a></li><li>→ <a href="#">Services</a></li><li>→ <a href="#">Projects</a></li><li>→ <a href="#">Contact</a></li>
    </ul>
  </div>
  <div class="footer-col col-connect">
    <h3>Connect With Us</h3>
    <div class="social"><span aria-label="Social profile"><i></i></span><span aria-label="Social profile"><i></i></span><span aria-label="Social profile"><i></i></span></div>
  </div>
  <div class="footer-col col-subscribe">
    <h3>Subscribe Us!</h3>
    <div class="subscribe-input">Enter email address</div>
    <div class="subscribe-btn">Subscribe</div>
  </div>
  <p class="copyright">Copyright ©2020 BRENVOLTFUND All rights reserved</p>
</footer>

</body>
</html>
```